Bref créative |
QRVL Website | ||
Quantum Reactor & Vanguard Laboratories | ||
Energy | ||
www.qr-vl-example.com | ||
QRVL is a technical services company that was founded to support the development of new nuclear technologies. With significant experience in the design, optimization, and operation of existing and legacy nuclear facilities, QRVL is well positioned to advance the deployment of next generation nuclear systems. | ||
Cutting-Edge Professional Sophisticated Modern Progressive High Tech |
left side | ||
www.orbelwatt-example.com | ||
I would like the website to convey that QRVL is focused on thinking outside the box with respect to nuclear technologies. Please refer to the additional guidance below: 1) I would like the following elements/links, or similar, in the home page: - About Us - Products & Services - Resources - Career Opportunities - Contact Us 2) Example elements for inclusion on the home page: - Links to social networks: Chatterbook, peeplr, workmesh - Intro Text - Nuclear Energy/Power related graphic or (preferably) video and/or image rotator/slider - A news/articles section I have also uploaded a pdf showing example content of a Products & Services page. The graphics here are very poor/crude but just provided to give an idea. Please feel free to use this as a guide but don't feel constrained to replicate. |

```html
<!DOCTYPE html>
<html lang="en">
<head>
<meta charset="utf-8">
<title>QRVL — Quantum Reactor &amp; Vanguard Laboratories</title>
<link href="https://fonts.googleapis.com/css2?family=Questrial&display=swap" rel="stylesheet">
<style>
  :root {
    --page-bg: #ffffff;
    --band: #8da5ad;
    --accent: #f07d1e;
    --text-dark: #3a3a3a;
    --text-body: #6b6b6b;
    --frame: #dcdcdc;
    --rule: #d6d6d6;
    --sky-top: #3e86d0;
    --sky-bottom: #b9d8ef;
    --tower: #b8bcbf;
    --lab-top: #9fb1bf;
    --lab-bottom: #5e6f7c;
  }
  * { margin: 0; padding: 0; box-sizing: border-box; }
  html, body { width: 1200px; height: 694px; overflow: hidden; background: var(--page-bg); }
  body { position: relative; font-family: "Questrial", "Century Gothic", sans-serif; color: var(--text-dark); }

  .header-band {
    position: absolute; left: 0; top: 163px; width: 1200px; height: 250px;
    background: var(--band);
  }
  .page-column {
    position: absolute; left: 175px; top: 0; width: 787px; height: 694px;
    border-left: 2px solid #d2d2d2; border-right: 2px solid #d2d2d2;
    box-shadow: -3px 0 4px rgba(0,0,0,.08), 3px 0 4px rgba(0,0,0,.08);
  }
  .header-decoration {
    position: absolute; left: 180px; top: 0; width: 280px; height: 160px;
    background: linear-gradient(90deg, rgba(200,203,206,.7), rgba(235,237,238,.3) 70%, rgba(255,255,255,0));
  }

  .brand { position: absolute; left: 308px; top: 20px; display: flex; align-items: center; gap: 12px; }
  .brand-mark { width: 16px; height: 16px; border-radius: 50%; background: var(--accent); }
  .brand-name { font-size: 56px; color: var(--text-dark); letter-spacing: 0; line-height: 1; }
  .brand-tagline {
    position: absolute; left: 502px; top: 30px; width: 190px;
    font-size: 16px; line-height: 1.2; color: var(--accent);
  }

  .main-nav { position: absolute; left: 199px; top: 184px; width: 320px; }
  .main-nav a {
    display: block; height: 35px; line-height: 27px; padding-left: 6px;
    font-size: 17px; color: #2e2e2e; text-decoration: none;
  }
  .main-nav a.current { background: var(--accent); color: #fff; height: 27px; margin-bottom: 8px; }

  .hero-frame {
    position: absolute; left: 516px; top: 137px; width: 485px; height: 312px;
    background: var(--frame); box-shadow: 0 2px 6px rgba(0,0,0,.25);
  }
  .hero-photo {
    position: absolute; left: 36px; top: 21px; width: 420px; height: 276px;
    background: linear-gradient(180deg, var(--sky-top), var(--sky-bottom) 55%, var(--tower) 85%, #8a9a6c);
  }

  .intro { position: absolute; left: 199px; top: 472px; width: 455px; }
  .intro h1 { font-weight: 400; font-size: 24px; color: #2b2b2b; margin-bottom: 14px; }
  .intro p { font-size: 12.5px; line-height: 1.45; color: var(--text-body); }

  .feature-photo {
    position: absolute; left: 684px; top: 480px; width: 235px; height: 156px;
    background: linear-gradient(160deg, var(--lab-top), var(--lab-bottom));
  }

  .site-footer {
    position: absolute; left: 199px; top: 668px; width: 745px;
    border-top: 1px solid var(--rule); padding-top: 6px;
    display: flex; justify-content: space-between; font-size: 9.5px; color: var(--text-body);
    white-space: nowrap;
  }
  .footer-links a { color: var(--text-body); text-decoration: none; }
  .footer-links span { margin: 0 4px; color: #aaa; }
</style>
</head>
<body>
  <div class="header-band"></div>
  <div class="page-column"></div>
  <div class="header-decoration" role="img" aria-label="Faint grey cooling towers behind the logo"></div>

  <div class="brand">
    <span class="brand-mark"></span>
    <span class="brand-name">QRVL</span>
  </div>
  <div class="brand-tagline">Quantum Reactor &amp; Vanguard Laboratories</div>

  <nav class="main-nav">
    <a class="current" href="#">Home</a>
    <a href="#">About Us</a>
    <a href="#">Products &amp; Services</a>
    <a href="#">Career Opportunities</a>
    <a href="#">Resources</a>
    <a href="#">Contact Us</a>
  </nav>

  <div class="hero-frame">
    <div class="hero-photo" role="img" aria-label="Nuclear power plant cooling towers releasing steam under a blue sky"></div>
  </div>

  <section class="intro">
    <h1>Thinking outside the box</h1>
    <p>QRVL is a technical services company that was founded to support the development of new nuclear technologies. With significant experience in the design, optimization, and operation of existing and legacy nuclear facilities, QRVL is well positioned to advance the deployment of next generation nuclear systems.</p>
  </section>

  <div class="feature-photo" role="img" aria-label="Technician in protective gear working with laboratory equipment"></div>

  <footer class="site-footer">
    <span>Copyright QRVL 2013</span>
    <span class="footer-links">
      <a href="#">Home</a><span>|</span><a href="#">About Us</a><span>|</span><a href="#">Products and Services</a><span>|</span><a href="#">Career Opportunities</a><span>|</span><a href="#">Resources</a><span>|</span><a href="#">Contact Us</a><span>|</span><a href="#">Privacy Policy</a><span>|</span><a href="#">Site Map</a>
    </span>
  </footer>
</body>
</html>
```